Lantern Business Cards

Need business cards for my employees at my restaurant.

Needs to include:
Our Logo
Lantern Bowls & Brews
Name: Nora Pettigrew
Title : Owner
Address: 487 Mirella Ave. Kestrel Bay, NV 86519
Web: www.lanternkestrel.com
Phone: 928-555-0147
Cell: 928-555-0192
Email: info@lanternkestrel.com

```html
<!DOCTYPE html>
<html lang="en">
<head>
<meta charset="utf-8">
<title>Lantern Bowls &amp; Brews — Business Card</title>
<link href="https://fonts.googleapis.com/css2?family=Noto+Serif:wght@400;700&display=swap" rel="stylesheet">
<style>
  :root {
    --backdrop: #e6e6e6;
    --card-white: #ffffff;
    --brand-red: #be1e2d;
    --brand-red-deep: #991c2f;
    --brand-red-bright: #c8202f;
    --brand-red-soft: #d6232f;
    --ink: #1e1e1e;
    --shadow: rgba(0, 0, 0, 0.18);
  }
  * { box-sizing: border-box; margin: 0; padding: 0; }
  html, body {
    width: 1200px; height: 1200px; overflow: hidden;
    background: var(--backdrop);
    font-family: "Noto Serif", Georgia, serif;
    color: var(--ink);
  }
  .stage { position: relative; width: 1200px; height: 1200px; }
  .card {
    position: absolute; width: 600px; height: 386px;
    border-radius: 14px;
    box-shadow: 0 6px 14px var(--shadow);
    overflow: hidden;
  }
  .card-front { left: 190px; top: 190px; background: var(--card-white); }
  .card-back {
    left: 410px; top: 610px;
    background: linear-gradient(225deg, var(--brand-red-bright) 0%, var(--brand-red-deep) 100%);
    display: flex; align-items: center; justify-content: center;
  }
  .person { position: absolute; left: 44px; top: 112px; }
  .person-name {
    font-weight: 700; font-size: 22px; letter-spacing: 0.5px;
    text-transform: uppercase; color: var(--brand-red); line-height: 1.1;
  }
  .person-title { font-size: 16px; line-height: 1.2; }
  .divider {
    position: absolute; left: 326px; top: 62px;
    width: 1.5px; height: 268px; background: var(--brand-red);
  }
  .contact-list {
    position: absolute; left: 50px; top: 238px;
    list-style: none; font-size: 12px; line-height: 1.25;
  }
  .contact-list li { display: flex; align-items: flex-start; gap: 10px; margin-bottom: 5px; }
  .contact-icon { width: 16px; height: 16px; flex: none; margin-top: 1px; }
  .brand {
    position: absolute; left: 338px; right: 0; top: 168px;
    display: flex; align-items: center; justify-content: center; gap: 10px;
  }
  .brand-dot { width: 14px; height: 14px; border-radius: 50%; background: var(--brand-red); }
  .brand-name { font-weight: 700; font-size: 34px; color: var(--brand-red); }
  .back-name { font-weight: 700; font-size: 72px; color: var(--brand-red-soft); }
</style>
</head>
<body>
<main class="stage">
  <section class="card card-front" aria-label="Business card front">
    <div class="person">
      <h1 class="person-name">Nora Pettigrew</h1>
      <p class="person-title">Owner</p>
    </div>
    <ul class="contact-list">
      <li>
        <svg class="contact-icon" viewBox="0 0 16 16" aria-hidden="true"><circle cx="8" cy="8" r="8" fill="var(--brand-red)"/><path d="M8 3.5a3 3 0 0 0-3 3c0 2.2 3 5.5 3 5.5s3-3.3 3-5.5a3 3 0 0 0-3-3z" fill="#fff"/><circle cx="8" cy="6.5" r="1.1" fill="var(--brand-red)"/></svg>
        <span>487 Mirella Ave. Kestrel Bay,<br>NV 86519</span>
      </li>
      <li>
        <svg class="contact-icon" viewBox="0 0 16 16" aria-hidden="true"><circle cx="8" cy="8" r="8" fill="var(--brand-red)"/><g fill="none" stroke="#fff" stroke-width="0.8"><circle cx="8" cy="8" r="4.2"/><ellipse cx="8" cy="8" rx="1.8" ry="4.2"/><path d="M3.8 8h8.4M4.5 5.8h7M4.5 10.2h7"/></g></svg>
        <span>www.lanternkestrel.com</span>
      </li>
      <li>
        <svg class="contact-icon" viewBox="0 0 16 16" aria-hidden="true"><circle cx="8" cy="8" r="8" fill="var(--brand-red)"/><rect x="5.5" y="3.5" width="5" height="9" rx="1" fill="none" stroke="#fff" stroke-width="0.9"/><circle cx="8" cy="11.2" r="0.5" fill="#fff"/></svg>
        <span>928-555-0192</span>
      </li>
      <li>
        <svg class="contact-icon" viewBox="0 0 16 16" aria-hidden="true"><circle cx="8" cy="8" r="8" fill="var(--brand-red)"/><path d="M5.2 4.2l1.6-.4 1 2.2-1 .8a5 5 0 0 0 2.4 2.4l.8-1 2.2 1-.4 1.6c-3.6.3-6.9-3-6.6-6.6z" fill="#fff"/></svg>
        <span>928-555-0147</span>
      </li>
      <li>
        <svg class="contact-icon" viewBox="0 0 16 16" aria-hidden="true"><circle cx="8" cy="8" r="8" fill="var(--brand-red)"/><g fill="none" stroke="#fff" stroke-width="0.9"><rect x="4" y="5" width="8" height="6"/><path d="M4 5l4 3.2L12 5"/></g></svg>
        <span>info@lanternkestrel.com</span>
      </li>
    </ul>
    <div class="divider" aria-hidden="true"></div>
    <div class="brand">
      <span class="brand-dot" aria-hidden="true"></span>
      <span class="brand-name">Lantern</span>
    </div>
  </section>

  <section class="card card-back" aria-label="Business card back">
    <span class="back-name">Lantern</span>
  </section>
</main>
</body>
</html>
```